Brandt Family Motto/Mission Statement

We are creating a poster to be hung in our home with several purpose statements for our family (last name Brandt, and "The Brandt Family" should be included in the poster prominently). The text that we want included is in the attached file.

Our kids range in age from 8 to 17, so we are looking for something that is homey and cheerful, but fairly bold and oriented to older kids (and not so much younger kids).

I've attached a couple of example poster/statements that we generally like. Overall color scheme could include blues and greens and possibly some brown.

Anticipated size of this poster would be 18"x24" with a portrait orientation.

```html
<!DOCTYPE html>
<html lang="en">
<head>
<meta charset="utf-8">
<title>The Brandt Family – Purpose Statements</title>
<link rel="stylesheet" href="https://fonts.googleapis.com/css2?family=Abril+Fatface&family=Alfa+Slab+One&family=Bebas+Neue&family=Josefin+Sans:ital,wght@0,300;1,300&family=Oswald:wght@200&family=Playfair+Display:wght@400&family=Poppins:wght@800&display=swap">
<style>
  :root {
    --plum: #6b2438;
    --teal: #13968b;
    --lime: #a9c43a;
    --slate: #869fb2;
    --graphite: #646466;
    --brick: #8b3532;
    --mint: #54be9c;
    --ink: #111111;
    --paper: #ffffff;
    --r: 133px;
  }
  html, body {
    margin: 0;
    padding: 0;
    width: 1200px;
    height: 856px;
    overflow: hidden;
    background: var(--paper);
  }
  .poster {
    position: relative;
    width: 1200px;
    height: 856px;
  }
  .value {
    position: absolute;
    width: calc(var(--r) * 2);
    height: calc(var(--r) * 2);
    margin: calc(var(--r) * -1) 0 0 calc(var(--r) * -1);
    border-radius: 50%;
    display: flex;
    flex-direction: column;
    align-items: center;
    justify-content: center;
    color: var(--paper);
    text-align: center;
    text-transform: uppercase;
    line-height: 1;
  }
  .value span { display: block; white-space: nowrap; }

  .bebas { font-family: "Bebas Neue", sans-serif; }
  .thin { font-family: "Josefin Sans", sans-serif; font-weight: 300; }
  .heavy { font-family: "Poppins", sans-serif; font-weight: 800; }
  .fat { font-family: "Abril Fatface", serif; }
  .slab { font-family: "Alfa Slab One", serif; }
  .condensed { font-family: "Oswald", sans-serif; font-weight: 200; }
  .outline {
    color: transparent;
    -webkit-text-stroke: 1.2px var(--paper);
  }

  .value--learn { left: 133px; top: 133px; background: var(--plum); }
  .value--learn .bebas { font-size: 44px; }
  .value--learn .thin { font-size: 28px; letter-spacing: 0.6em; margin: 6px 0 4px 0.6em; }

  .value--adventure { left: 441px; top: 133px; background: var(--teal); }
  .value--adventure .lead { font-size: 30px; }
  .value--adventure .small { font-size: 13px; letter-spacing: 0.78em; margin: 2px 0 2px 0.78em; }
  .value--adventure .outline { font-size: 46px; }
  .value--adventure .big { font-size: 54px; }

  .value--positive { left: 759px; top: 133px; background: var(--lime); }
  .value--positive .thin { font-size: 24px; }
  .value--positive .heavy { font-size: 20px; margin: 6px 0; }

  .value--fit { left: 1065px; top: 133px; background: var(--slate); }
  .value--fit .fat { font-size: 32px; letter-spacing: 0.02em; }
  .value--fit .thin { font-size: 44px; margin-top: 2px; }

  .value--kindness { left: 286px; top: 450px; background: var(--graphite); }
  .value--kindness .outline { font-family: "Josefin Sans", sans-serif; font-weight: 300; font-size: 23px; }
  .value--kindness .slab { font-size: 23px; letter-spacing: 0.1em; margin: 8px 0 6px 0.1em; }
  .value--kindness .condensed { font-size: 40px; letter-spacing: 0.15em; margin-left: 0.15em; }

  .value--humor { left: 597px; top: 450px; background: var(--brick); }
  .value--humor .heavy { font-size: 27px; }
  .value--humor .outline { font-family: "Alfa Slab One", serif; font-size: 26px; margin: 6px 0; }
  .value--humor .bebas { font-size: 31px; }

  .value--integrity { left: 913px; top: 450px; background: var(--mint); }
  .value--integrity .fat { font-size: 17px; letter-spacing: 0.04em; }
  .value--integrity .thin { font-size: 21px; font-style: italic; margin: 7px 0; }
  .value--integrity .outline { font-family: "Alfa Slab One", serif; font-size: 25px; }

  .family-name {
    position: absolute;
    left: 0;
    top: 640px;
    width: 1200px;
    margin: 0;
    font-weight: 400;
    color: var(--ink);
    line-height: 1;
    display: flex;
    flex-direction: column;
    align-items: center;
  }
  .family-name__the,
  .family-name__family {
    font-family: "Playfair Display", serif;
    font-size: 34px;
    width: 210px;
    display: flex;
    justify-content: space-between;
  }
  .family-name__surname {
    font-family: "Bebas Neue", sans-serif;
    font-size: 122px;
    display: block;
    margin: 4px 0 -6px;
  }
</style>
</head>
<body>
<main class="poster">
  <div class="value value--learn">
    <span class="bebas">We love to</span>
    <span class="thin">Learn</span>
    <span class="bebas">New things</span>
  </div>
  <div class="value value--adventure">
    <span class="bebas lead">We create adventure</span>
    <span class="thin small">and choose</span>
    <span class="bebas outline">Experiences</span>
    <span class="bebas big">Over things</span>
  </div>
  <div class="value value--positive">
    <span class="thin">We like to look</span>
    <span class="heavy">At life through a</span>
    <span class="thin">Positive lens</span>
  </div>
  <div class="value value--fit">
    <span class="fat">We commit</span>
    <span class="thin">To be fit</span>
  </div>
  <div class="value value--kindness">
    <span class="outline">Kindness guides</span>
    <span class="slab">Our words</span>
    <span class="condensed">And deeds</span>
  </div>
  <div class="value value--humor">
    <span class="heavy">Our days are</span>
    <span class="outline">Brightened</span>
    <span class="bebas">By a sense of humor</span>
  </div>
  <div class="value value--integrity">
    <span class="fat">We do what is right</span>
    <span class="thin">Even when no one</span>
    <span class="outline">Is watching</span>
  </div>

  <h1 class="family-name" aria-label="The Brandt Family">
    <span class="family-name__the"><span>T</span><span>H</span><span>E</span></span>
    <span class="family-name__surname">BRANDT</span>
    <span class="family-name__family"><span>F</span><span>A</span><span>M</span><span>I</span><span>L</span><span>Y</span></span>
  </h1>
</main>
</body>
</html>
```